Modern Yoga Studio Timetable and Flyer Design

We have a comprehensive class timetable and we are wanting to a clean modern look for our Spring timetable.

We require a double sided flyer with our class timetable included.
We would prefer an A5 size (postcard) or DL (1/3 A4).

We would like the final flyer to have.
Side A : Yoga image, logo

Fennel Stretch Hall
address: 4/71 Wexcombe Lane, Pelharton
website: fennelstretch.com.au
mobile: 0471 296 814

Side B: Clear easy to read timetable with a break down of class types and website.

We would also like to have a copy of the timetable itself as a separate jpg or pdf for use on our website to download.

Thank you.
Yours kindly,
Nell

I have attached a sample of another timetable of which I like the look and feel of, however this is just a guide. I've also attached our 'new' schedule in WORD plus uploaded our last design of the front.
Updates

Target Market(s)

Women aged 30-45

Industry/Entity Type

Health And Wellness

Font styles to use
Other font styles liked:
• Brandon Grotesque, Jenna Sue

Colors
6c459b
33a6d7
ffffff

Requirements
Must have
• A definitive colour to decipher between different class types on our timetable. Where each colour represents a different class type. Colours and layouts similar to our website design, see www.fennelstretch.com.au
Nice to have
• I've included a design of another studio whose timetable design I like. One of our own yoga images instead of a stock image.
Should not have
• No dark gridlines between the cells/boxes in the timetables. Please don't use stock yoga images.

```html
<!DOCTYPE html>
<html lang="en">
<head>
<meta charset="utf-8">
<title>Fennel Stretch Hall – Spring Flyer</title>
<link href="https://fonts.googleapis.com/css2?family=Source+Sans+3:wght@400;600;700&display=swap" rel="stylesheet">
<style>
  :root {
    --stage: #262626;
    --paper: #ffffff;
    --brand-purple: #6c459b;
    --brand-blue: #33a6d7;
    --ink-blue: #2f7fc4;
    --ink-navy: #24609e;
    --frame: #d9d4ee;
    --slot: #eef3f9;
    --slot-gap: #ffffff;
    --muted: #4a5568;
    --rise: #8cbf58;
    --vinyasa: #6a6fb8;
    --slow: #8a8fd0;
    --mum: #8fc6ea;
    --pregnancy: #4ea89a;
    --kids-older: #efa03e;
    --kids-young: #f1de48;
    --teens: #e0773a;
    --flow-restore: #7e5aa8;
    --yin: #9b59a8;
    --wellness: #d65a6a;
  }
  * { box-sizing: border-box; margin: 0; padding: 0; }
  html, body { width: 1200px; height: 527px; overflow: hidden; }
  body {
    background: var(--stage);
    font-family: "Source Sans 3", "Helvetica Neue", Arial, sans-serif;
    display: flex;
    align-items: center;
    justify-content: center;
    gap: 40px;
  }

  /* ---------- Side A ---------- */
  .flyer-front {
    position: relative;
    width: 330px;
    height: 467px;
    background: var(--paper);
    overflow: hidden;
  }
  .flyer-front .artwork { position: absolute; inset: 0; }
  .brand-name {
    position: absolute;
    top: 70px;
    left: 0;
    right: 0;
    text-align: center;
    font-size: 15px;
    font-weight: 400;
    letter-spacing: 5px;
    text-transform: lowercase;
    color: var(--brand-blue);
  }
  .studio-contact {
    position: absolute;
    right: 26px;
    bottom: 44px;
    text-align: right;
    color: var(--ink-blue);
    line-height: 1.15;
  }
  .studio-contact .studio-name { font-size: 21px; font-weight: 700; }
  .studio-contact .studio-address,
  .studio-contact .studio-web { font-size: 14px; font-weight: 600; }
  .studio-contact .studio-phone { font-size: 17px; font-weight: 700; color: var(--ink-navy); }

  /* ---------- Side B ---------- */
  .flyer-back {
    width: 660px;
    height: 467px;
    background: linear-gradient(160deg, #ffffff 55%, #e9f0f9 100%);
    padding: 18px 21px 16px;
    display: flex;
    flex-direction: column;
  }
  .timetable-title {
    text-align: center;
    color: var(--brand-blue);
    font-size: 18px;
    font-weight: 700;
    letter-spacing: 1px;
    text-transform: uppercase;
    margin-bottom: 10px;
  }
  .timetable {
    position: relative;
    display: grid;
    grid-template-columns: 64px repeat(7, 76px);
    grid-template-rows: 18px repeat(13, 22px);
    gap: 3px;
  }
  .timetable .slots {
    grid-column: 2 / 9;
    grid-row: 2 / 15;
    background:
      repeating-linear-gradient(90deg, transparent 0 76px, var(--slot-gap) 76px 79px),
      repeating-linear-gradient(180deg, transparent 0 22px, var(--slot-gap) 22px 25px),
      var(--slot);
  }
  .day, .time {
    font-size: 8.5px;
    font-weight: 600;
    color: var(--muted);
    text-transform: uppercase;
    display: flex;
    align-items: center;
  }
  .day { justify-content: center; grid-row: 1; }
  .time { justify-content: flex-end; padding-right: 8px; grid-column: 1; }
  .class {
    position: relative;
    display: flex;
    align-items: center;
    justify-content: center;
    text-align: center;
    color: #fff;
    font-size: 7.5px;
    font-weight: 600;
    line-height: 1.05;
    text-transform: uppercase;
  }
  .class.booking::after {
    content: "★";
    position: absolute;
    top: 0;
    right: 2px;
    font-size: 6px;
  }
  .rise { background: var(--rise); }
  .vinyasa { background: var(--vinyasa); }
  .slow { background: var(--slow); }
  .mum { background: var(--mum); }
  .pregnancy { background: var(--pregnancy); }
  .kids-older { background: var(--kids-older); }
  .kids-young { background: var(--kids-young); color: #6b5a10; }
  .teens { background: var(--teens); }
  .flow-restore { background: var(--flow-restore); }
  .yin { background: var(--yin); }
  .wellness { background: var(--wellness); }

  .timetable-footer {
    margin-top: auto;
    display: flex;
    justify-content: space-between;
    align-items: center;
    padding: 0 6px;
  }
  .booking-note { font-size: 9px; color: var(--muted); text-transform: uppercase; }
  .timetable-web { font-size: 12px; font-weight: 700; color: var(--brand-blue); }
</style>
</head>
<body>

  <section class="flyer-front">
    <svg class="artwork" width="330" height="467" viewBox="0 0 330 467">
      <defs>
        <linearGradient id="photo-tone" x1="0" y1="0" x2="0" y2="1">
          <stop offset="0" stop-color="#c9c2d3"/>
          <stop offset="0.45" stop-color="#9478bf"/>
          <stop offset="0.8" stop-color="#b9a9e0"/>
          <stop offset="1" stop-color="#e6ebf8"/>
        </linearGradient>
        <linearGradient id="wave-tone" x1="0" y1="0" x2="0" y2="1">
          <stop offset="0" stop-color="#8fb7ea" stop-opacity="0.4"/>
          <stop offset="0.6" stop-color="#3f83d6"/>
          <stop offset="1" stop-color="#6aa3e4" stop-opacity="0.7"/>
        </linearGradient>
        <linearGradient id="ornament-tone" x1="0" y1="0" x2="1" y2="1">
          <stop offset="0" stop-color="#5b3a8c"/>
          <stop offset="1" stop-color="#c9c9cf"/>
        </linearGradient>
      </defs>
      <path role="img" aria-label="Decorative ornament in purple and silver tones"
            d="M60 0 H250 C245 40 200 62 155 62 C110 62 65 40 60 0 Z" fill="url(#ornament-tone)"/>
      <path role="img" aria-label="Studio photograph of a yoga pose on a mat, tinted purple"
            d="M12 96 H262 C236 170 318 210 296 262 C272 318 160 322 128 380 C112 410 110 440 108 467 H12 Z"
            fill="url(#photo-tone)"/>
      <path d="M262 96 C236 170 318 210 296 262 C272 318 160 322 128 380 C112 410 110 440 108 467"
            fill="none" stroke="url(#wave-tone)" stroke-width="14"/>
      <rect x="14" y="90" width="302" height="360" fill="none" stroke="var(--frame)" stroke-width="1.5"/>
    </svg>
    <div class="brand-name">fennel stretch hall</div>
    <address class="studio-contact" style="font-style:normal">
      <div class="studio-name">Fennel Stretch Hall</div>
      <div class="studio-address">4/71 Wexcombe Lane, Pelharton</div>
      <div class="studio-web">fennelstretch.com.au</div>
      <div class="studio-phone">0471 296 814</div>
    </address>
  </section>

  <section class="flyer-back">
    <h1 class="timetable-title">Fennel Stretch Spring Timetable</h1>
    <div class="timetable">
      <div class="slots"></div>

      <div class="day" style="grid-column:2">Mon</div>
      <div class="day" style="grid-column:3">Tue</div>
      <div class="day" style="grid-column:4">Wed</div>
      <div class="day" style="grid-column:5">Thu</div>
      <div class="day" style="grid-column:6">Fri</div>
      <div class="day" style="grid-column:7">Sat</div>
      <div class="day" style="grid-column:8">Sun</div>

      <div class="time" style="grid-row:2">5:45 AM</div>
      <div class="time" style="grid-row:3">9:00 AM</div>
      <div class="time" style="grid-row:4">9:15 AM</div>
      <div class="time" style="grid-row:5">9:30 AM</div>
      <div class="time" style="grid-row:6">10:30 AM</div>
      <div class="time" style="grid-row:7">11:00 AM</div>
      <div class="time" style="grid-row:8">12:15 PM</div>
      <div class="time" style="grid-row:9">4:00 PM</div>
      <div class="time" style="grid-row:10">4:45 PM</div>
      <div class="time" style="grid-row:11">5:00 PM</div>
      <div class="time" style="grid-row:12">6:00 PM</div>
      <div class="time" style="grid-row:13">6:15 PM</div>
      <div class="time" style="grid-row:14">7:00 PM</div>

      <div class="class rise booking" style="grid-column:3;grid-row:2">Rise &amp;<br>Shine</div>
      <div class="class rise booking" style="grid-column:5;grid-row:2">Rise &amp;<br>Shine</div>
      <div class="class vinyasa" style="grid-column:7;grid-row:3">Vinyasa<br>Flow</div>
      <div class="class yin" style="grid-column:8;grid-row:3">Yin</div>
      <div class="class vinyasa" style="grid-column:4;grid-row:4">Vinyasa<br>Flow</div>
      <div class="class slow" style="grid-column:6;grid-row:4">Slow<br>Flow</div>
      <div class="class pregnancy" style="grid-column:8;grid-row:4">Pregnancy</div>
      <div class="class slow" style="grid-column:3;grid-row:5">Slow<br>Flow</div>
      <div class="class mum" style="grid-column:7;grid-row:5">Mum &amp;<br>Baby</div>
      <div class="class mum booking" style="grid-column:5;grid-row:6">Mum &amp;<br>Baby</div>
      <div class="class pregnancy" style="grid-column:7;grid-row:6">Pregnancy</div>
      <div class="class slow" style="grid-column:8;grid-row:6">Slow<br>Flow</div>
      <div class="class kids-older" style="grid-column:6;grid-row:7">Kids<br>6-12</div>
      <div class="class kids-young booking" style="grid-column:7;grid-row:7">Kids<br>3-5</div>
      <div class="class teens" style="grid-column:6;grid-row:8">Teens<br>12-16</div>
      <div class="class teens" style="grid-column:7;grid-row:8">Teens<br>12-16</div>
      <div class="class flow-restore" style="grid-column:8;grid-row:8">Flow &amp;<br>Restore</div>
      <div class="class pregnancy" style="grid-column:8;grid-row:10">Pregnancy</div>
      <div class="class vinyasa booking" style="grid-column:5;grid-row:11">Vinyasa<br>Flow</div>
      <div class="class slow" style="grid-column:6;grid-row:11">Slow<br>Flow</div>
      <div class="class wellness booking" style="grid-column:8;grid-row:11">Women's<br>Wellness</div>
      <div class="class pregnancy booking" style="grid-column:4;grid-row:12">Pregnancy</div>
      <div class="class yin" style="grid-column:7;grid-row:12">Yin &amp;<br>Restore</div>
      <div class="class vinyasa" style="grid-column:5;grid-row:13">Vinyasa<br>Flow</div>
      <div class="class pregnancy" style="grid-column:6;grid-row:13">Pregnancy</div>
    </div>
    <footer class="timetable-footer">
      <span class="booking-note">★ Bookings essential</span>
      <span class="timetable-web">fennelstretch.com.au</span>
    </footer>
  </section>

</body>
</html>
```